Four Key Ledger Blueprint Presentation

I would like a flyer to hand out to participants at the speeches that we give. We are a CPA firm that specializes in entrepreneurs and realtors. We would like a flyer that looks crisp and clean, that integrates our logo and our company colors (shades of blue & gold). We would like the wording to be as laid out in the attached documents, but design is up to you. We would like a picture to go along with each point and are open to ideas. The flyer should be one page, preferably just the front.

Colors
3176b5
fee18a

Requirements
Must have
• Our logo and the wording supplied.
• A picture to go along with each topic.
Nice to have
• Images that pop, clean look, professional.
Should not have
• Look messy.

```html
<!DOCTYPE html>
<html lang="en">
<head>
<meta charset="utf-8">
<title>Four Key Ledger Blueprint Presentation</title>
<link href="https://fonts.googleapis.com/css2?family=EB+Garamond:wght@400;700&family=Libre+Baskerville:ital,wght@1,700&display=swap" rel="stylesheet">
<style>
  :root {
    --gold-light: #fee18a;
    --gold-pale: #fdf0c0;
    --blue: #3176b5;
    --blue-mid: #7fa6cf;
    --blue-pale: #c9d7e3;
    --band-dark: #8b7448;
    --ink: #141414;
  }
  * { margin: 0; padding: 0; box-sizing: border-box; }
  html, body { width: 846px; height: 1200px; overflow: hidden; }
  body { font-family: "EB Garamond", Garamond, serif; color: var(--ink); }

  .flyer {
    position: relative;
    width: 846px;
    height: 1200px;
    overflow: hidden;
    background:
      linear-gradient(160deg, var(--gold-light) 0%, var(--gold-pale) 28%, #e3e3d8 52%, var(--blue-pale) 66%, var(--blue-mid) 100%);
  }

  .swoosh { position: absolute; left: 0; top: 0; width: 846px; height: 1200px; }

  .brand {
    position: absolute;
    left: 62px;
    top: 70px;
    display: flex;
    align-items: center;
    gap: 12px;
    white-space: nowrap;
  }
  .brand-mark {
    width: 24px; height: 24px; border-radius: 50%;
    background: var(--blue);
    flex: none;
  }
  .brand-name {
    font-family: "EB Garamond", Garamond, serif;
    font-weight: 700;
    font-size: 40px;
    line-height: 1;
    color: var(--blue);
  }

  .tagline {
    position: absolute;
    left: 400px;
    top: 76px;
    font-family: "Libre Baskerville", Georgia, serif;
    font-style: italic;
    font-weight: 700;
    font-size: 18px;
    color: var(--ink);
  }

  .point {
    position: absolute;
    font-size: 18px;
    line-height: 21.7px;
    white-space: nowrap;
  }
  .tick { position: absolute; width: 36px; height: 36px; }

  .photo {
    position: absolute;
    border-radius: 50%;
    box-shadow: 0 2px 6px rgba(0,0,0,0.15);
  }
  .photo-money   { background: radial-gradient(circle at 60% 40%, #f4f1ec, #b89370 80%); }
  .photo-house   { background: radial-gradient(circle at 45% 45%, #a64b3a, #d9c9a8 75%); }
  .photo-ledger  { background: radial-gradient(circle at 50% 55%, #8d939a, #e8e6e2 75%); }
  .photo-deal    { background: radial-gradient(circle at 50% 50%, #3a3f4a, #e9ecef 75%); }
  .photo-family  { background: radial-gradient(circle at 50% 45%, #8a8580, #3d4760 80%); }
  .photo-student { background: radial-gradient(circle at 40% 45%, #5a4a40, #ecebe7 75%); }
  .photo-desk    { background: radial-gradient(circle at 55% 55%, #6e7176, #f0efec 75%); }
</style>
</head>
<body>
<main class="flyer">

  <svg class="swoosh" viewBox="0 0 846 1200" aria-hidden="true">
    <defs>
      <linearGradient id="baseBlue" x1="0" y1="0" x2="1" y2="1">
        <stop offset="0" stop-color="#5d8fc4"/>
        <stop offset="1" stop-color="#b7cadb"/>
      </linearGradient>
      <linearGradient id="bandGold" x1="0" y1="0" x2="1" y2="0">
        <stop offset="0" stop-color="#a58a58"/>
        <stop offset="0.5" stop-color="#c3a672"/>
        <stop offset="1" stop-color="#d8c08c"/>
      </linearGradient>
    </defs>
    <path d="M0,1078 C160,1120 460,1175 846,1206 L846,1200 L0,1200 Z" fill="url(#baseBlue)"/>
    <path d="M0,1066 C160,1108 460,1166 846,1200 L846,1206 C460,1175 160,1120 0,1078 Z" fill="#2f4f78" opacity="0.7"/>
    <path d="M0,876 C60,990 300,1100 846,1168 L846,1200 C460,1166 160,1108 0,1066 Z" fill="url(#bandGold)"/>
    <path d="M0,876 C60,990 300,1100 846,1168" fill="none" stroke="var(--band-dark)" stroke-width="1"/>
  </svg>

  <header>
    <div class="brand">
      <span class="brand-mark"></span>
      <span class="brand-name">Clearline Figures</span>
    </div>
    <p class="tagline">A Professional Accounting Corporation</p>
  </header>

  <svg class="tick" style="left:44px;top:216px" viewBox="0 0 36 36" aria-hidden="true"><path d="M3,19 L13,30 L33,4" fill="none" stroke="#111" stroke-width="4" stroke-linecap="round" stroke-linejoin="round"/></svg>
  <p class="point" style="left:111px;top:181px">We will first show you how to eliminate much of your<br>self-employment tax on your return by converting<br>your business into an S Corporation. &nbsp; A business<br>owner making over $120,000 per year can save about<br>$12,000 per year by doing this.</p>

  <svg class="tick" style="left:44px;top:336px" viewBox="0 0 36 36" aria-hidden="true"><path d="M3,19 L13,30 L33,4" fill="none" stroke="#111" stroke-width="4" stroke-linecap="round" stroke-linejoin="round"/></svg>
  <p class="point" style="left:111px;top:313px">We will show you how to get tax free income from<br>your corporation by renting you home to the corpora-<br>tion for the board meetings. &nbsp; Many of our clients are<br>getting up to $21,000 in tax free income which could<br>put $8,400 cash into your pocket.</p>

  <svg class="tick" style="left:44px;top:464px" viewBox="0 0 36 36" aria-hidden="true"><path d="M3,19 L13,30 L33,4" fill="none" stroke="#111" stroke-width="4" stroke-linecap="round" stroke-linejoin="round"/></svg>
  <p class="point" style="left:111px;top:444px">We will show you the easiest way to track your ex-<br>penses so that the only thing you will have to do to<br>have rock solid books is to take a picture of the receipt<br>and throw it away. &nbsp; It doesn’t get any better than<br>that.</p>

  <svg class="tick" style="left:44px;top:592px" viewBox="0 0 36 36" aria-hidden="true"><path d="M3,19 L13,30 L33,4" fill="none" stroke="#111" stroke-width="4" stroke-linecap="round" stroke-linejoin="round"/></svg>
  <p class="point" style="left:111px;top:572px">Next, we show you the importance of tax planning<br>and why it is critical to meet with your CPA before<br>the end of the year and not just when you do your tax<br>preparation.</p>

  <svg class="tick" style="left:44px;top:704px" viewBox="0 0 36 36" aria-hidden="true"><path d="M3,19 L13,30 L33,4" fill="none" stroke="#111" stroke-width="4" stroke-linecap="round" stroke-linejoin="round"/></svg>
  <p class="point" style="left:110px;top:688px">We will show you how to hire your children and get<br>$7,500 per child tax free. &nbsp; This will save you $3,000<br>per child in income tax reduction.</p>

  <svg class="tick" style="left:60px;top:812px" viewBox="0 0 36 36" aria-hidden="true"><path d="M3,19 L13,30 L33,4" fill="none" stroke="#111" stroke-width="4" stroke-linecap="round" stroke-linejoin="round"/></svg>
  <p class="point" style="left:126px;top:796px">We will discuss how to make your child’s college edu-<br>cation tax deductible. &nbsp; With college cost spiraling out<br>of control this is a biggie. &nbsp; Most of our clients have a<br>savings of about $12,000 per year of college.</p>

  <svg class="tick" style="left:170px;top:932px" viewBox="0 0 36 36" aria-hidden="true"><path d="M3,19 L13,30 L33,4" fill="none" stroke="#111" stroke-width="4" stroke-linecap="round" stroke-linejoin="round"/></svg>
  <p class="point" style="left:235px;top:916px">Our grand finale is to show you how to use, not one,<br>but two corporations to get a several hundred thou-<br>sand dollar tax deferral, get an interest free loan from<br>the government and use that money to grow your<br>business and your wealth.</p>

  <div class="photo photo-money" style="left:598px;top:126px;width:124px;height:124px" role="img" aria-label="Photo: stacks of coins with a dollar sign on top"></div>
  <div class="photo photo-house" style="left:588px;top:274px;width:120px;height:120px" role="img" aria-label="Photo: model house beside stacks of coins"></div>
  <div class="photo photo-ledger" style="left:628px;top:398px;width:112px;height:112px" role="img" aria-label="Photo: hands using a calculator and laptop"></div>
  <div class="photo photo-deal" style="left:576px;top:540px;width:120px;height:120px" role="img" aria-label="Photo: business handshake over a contract"></div>
  <div class="photo photo-family" style="left:674px;top:640px;width:120px;height:120px" role="img" aria-label="Photo: family meeting with an advisor"></div>
  <div class="photo photo-student" style="left:590px;top:756px;width:136px;height:136px" role="img" aria-label="Photo: college student studying in a classroom"></div>
  <div class="photo photo-desk" style="left:672px;top:924px;width:136px;height:136px" role="img" aria-label="Photo: car model, calculator and coins on a desk"></div>

</main>
</body>
</html>
```